Company or website name
- Plate Rover Restaurant Delivery Service LLC
- Links to the website
- We are a restaurant marketing and delivery company. We market restaurants and deliver their food.
- Other Facts

```html
<!DOCTYPE html>
<html lang="en">
<head>
<meta charset="utf-8">
<title>Plate Rover – About Us</title>
<link rel="stylesheet" href="https://fonts.googleapis.com/css2?family=Kaushan+Script&family=Arimo:wght@400;700&display=swap">
<style>
  :root {
    --wood-dark: #24110a;
    --wood-mid: #3b1e12;
    --brick-red: #b52a13;
    --brick-red-deep: #9c2110;
    --amber: #e9a51c;
    --amber-deep: #d98f12;
    --badge-red: #b8261a;
    --ink: #140a05;
    --white: #ffffff;
    --logo-green: #1f9a3c;
  }
  * { box-sizing: border-box; margin: 0; padding: 0; }
  html, body { width: 1200px; height: 750px; overflow: hidden; }
  body {
    position: relative;
    background: linear-gradient(100deg, var(--wood-mid) 0%, var(--wood-dark) 35%, var(--wood-mid) 60%, var(--wood-dark) 100%);
    font-family: "Arimo", Arial, sans-serif;
    color: var(--ink);
  }
  .panels { position: absolute; inset: 0; }
  .panel-shape { stroke: var(--white); stroke-width: 6; stroke-linejoin: round; filter: drop-shadow(0 0 3px rgba(0,0,0,.6)); }

  .brand {
    position: absolute;
    display: flex; align-items: center; justify-content: center;
    border-radius: 50%;
    background: var(--logo-green);
    color: var(--white);
    font-weight: 700;
    text-align: center;
    line-height: 1.05;
  }
  .brand--about { left: 127px; top: 87px; width: 210px; height: 210px; font-size: 40px; }
  .brand--contact { left: 425px; top: 493px; width: 170px; height: 170px; font-size: 32px; }

  .script-heading { position: absolute; font-family: "Kaushan Script", cursive; color: var(--ink); font-weight: 400; }

  .about-heading { left: 435px; top: 42px; font-size: 34px; }
  .about-copy { position: absolute; left: 427px; top: 104px; width: 728px; font-size: 16.4px; line-height: 18.8px; text-align: justify; }
  .about-copy p { margin-bottom: 17px; }

  .tips { position: absolute; top: 470px; width: 260px; }
  .tips--order { left: 82px; }
  .tips--facts { left: 890px; }
  .tips h2 { font-family: "Kaushan Script", cursive; font-weight: 400; font-size: 24px; text-align: center; margin-bottom: 16px; }
  .tips ol { list-style: none; }
  .tips li { display: flex; align-items: center; gap: 10px; height: 26px; margin-bottom: 22px; font-family: "Kaushan Script", cursive; font-size: 14px; white-space: nowrap; }
  .tips .num { flex: none; width: 24px; height: 24px; border-radius: 50%; background: var(--badge-red); color: var(--white); display: flex; align-items: center; justify-content: center; font-size: 13px; box-shadow: 0 0 0 2px rgba(255,255,255,.35); }
  .tips--order li { padding-left: 42px; }
  .tips--facts li { padding-left: 40px; }

  .contact-heading { left: 684px; top: 460px; font-size: 22px; }
  .contact-details { position: absolute; left: 635px; top: 508px; font-size: 13px; line-height: 16.4px; }
  .contact-details p { margin-bottom: 16px; }
  .contact-details .web { position: absolute; top: 198px; white-space: nowrap; }
</style>
</head>
<body>
  <svg class="panels" width="1200" height="750" viewBox="0 0 1200 750" aria-hidden="true">
    <defs>
      <linearGradient id="redFill" x1="0" y1="0" x2="0" y2="1">
        <stop offset="0" stop-color="var(--brick-red)"/>
        <stop offset="1" stop-color="var(--brick-red-deep)"/>
      </linearGradient>
      <linearGradient id="amberFill" x1="0" y1="0" x2="0" y2="1">
        <stop offset="0" stop-color="var(--amber)"/>
        <stop offset="1" stop-color="var(--amber-deep)"/>
      </linearGradient>
    </defs>
    <path class="panel-shape" fill="url(#redFill)" d="M100,27 H1162 V410 H168 L102,443 Z"/>
    <path class="panel-shape" fill="url(#amberFill)" d="M327,652 A140,140 0 1,0 278,696 L345,705 Z"/>
    <path class="panel-shape" fill="url(#amberFill)" d="M405,425 L440,440 H822 V738 H405 Z"/>
    <path class="panel-shape" fill="url(#amberFill)" d="M905,652 A140,140 0 1,1 954,696 L855,705 Z"/>
  </svg>

  <section class="about">
    <div class="brand brand--about">Plate<br>Rover</div>
    <h1 class="script-heading about-heading">About Us:</h1>
    <div class="about-copy">
      <p>Lorem ipsum dolor sit amet, consectetur adipisicing elit, sed do eiusmod tempor incididunt ut labore et dolore magna aliqua. Ut enim ad minim veniam, quis nostrud exercitation ullamco laboris nisi ut aliquip ex ea commodo consequat. Duis aute irure dolor in reprehenderit in voluptate velit esse cillum dolore eu fugiat nulla pariatur. Excepteur sint occaecat cupidatat non proident, sunt in culpa qui officia deserunt mollit anim id est laborum</p>
      <p>Lorem ipsum dolor sit amet, consectetur adipisicing elit, sed do eiusmod tempor incididunt ut labore et dolore magna aliqua. Ut enim ad minim veniam, quis nostrud exercitation ullamco laboris nisi ut aliquip ex ea commodo consequat. Duis aute irure dolor in reprehenderit in voluptate velit esse cillum dolore eu fugiat nulla pariatur. Excepteur sint occaecat cupidatat non proident, sunt in culpa qui officia deserunt mollit anim id est laborum</p>
      <p>Lorem ipsum dolor sit amet, consectetur adipisicing elit, sed do eiusmod tempor incididunt ut labore et dolore magna aliqua. Ut enim ad minim veniam, quis nostrud exercitation ullamco laboris nisi ut aliquip ex ea commodo consequat..</p>
    </div>
  </section>

  <section class="tips tips--order">
    <h2>How to Order:</h2>
    <ol>
      <li><span class="num">1.</span>Lorem ipsum dolor sit amet</li>
      <li><span class="num">2.</span>Lorem ipsum dolor sit amet</li>
      <li><span class="num">3.</span>Lorem ipsum dolor sit amet</li>
    </ol>
  </section>

  <section class="contact">
    <div class="brand brand--contact">Plate<br>Rover</div>
    <h2 class="script-heading contact-heading">Contact Us:</h2>
    <div class="contact-details">
      <p>Lorem Ipsum,<br>No.11, Dolor Sit amet,<br>Lorem Ipsum- 111 111</p>
      <p>Phone:</p>
      <p>ABCD- 111- 12345678<br>EFGH- 111- 12345678<br>IJKL-&nbsp;&nbsp;&nbsp; 111- 12345678<br>MNOP- 111- 12345678<br>QRST-&nbsp; 111- 12345678</p>
      <span class="web">http://www.platerover.com</span>
    </div>
  </section>

  <section class="tips tips--facts">
    <h2>Did you know:</h2>
    <ol>
      <li><span class="num">1.</span>Lorem ipsum dolor sit amet</li>
      <li><span class="num">2.</span>Lorem ipsum dolor sit amet</li>
      <li><span class="num">3.</span>Lorem ipsum dolor sit amet</li>
    </ol>
  </section>
</body>
</html>
```